I am looking for a stand-out cover that sings out to new parents. The category is very pastel with limited compelling covers that would make me want to buy a book. This book will be used often in the first 12 months of baby's life - so must be strong enough to sit on the bedside table or on the coffee table to inspire reading. It will be a popular gift - so needs to look credible, "pick-up-able" and loveable.

The Book Title is - The Cradle Compass to Infancy's Opening Seasons: Grounded, Research-Led Methods on Rest, Nourishment, Protection plus Growing Assurance
The Size is - 8.5 x 11 in
Book description to be provided to final design for inclusion
Some examples of book covers in this category attached. Thanks

```html
<!DOCTYPE html>
<html lang="en">
<head>
<meta charset="utf-8">
<title>The Cradle Compass to Infancy's Opening Seasons – Cover</title>
<link rel="stylesheet" href="https://fonts.googleapis.com/css2?family=Oswald:wght@300;400;600&family=Poppins:wght@400&display=swap">
<style>
  :root{
    --stage:#ffffff;
    --paper:#ffffff;
    --coral:#f08a80;
    --coral-soft:#f6a79c;
    --sun:#f2c75c;
    --sun-soft:#f8dc8f;
    --cream:#fdf1dc;
    --teal:#2a8a9a;
    --line-sun:#f0c860;
    --line-coral:#f0958a;
  }
  *{margin:0;padding:0;box-sizing:border-box}
  html,body{width:1200px;height:574px;overflow:hidden;background:var(--stage)}
  .cover{
    position:absolute;left:395px;top:22px;width:410px;height:530px;
    background:var(--paper);
    box-shadow:0 3px 10px rgba(0,0,0,.12);
    overflow:hidden;
  }
  .cover-frame{position:absolute;inset:0}
  .title{position:absolute;left:0;right:0;text-align:center;font-family:"Oswald",sans-serif}
  .title-kicker{
    top:24px;font-weight:400;font-size:19px;letter-spacing:15px;color:var(--teal);
    padding-left:40px;line-height:1;
  }
  .title-main{
    top:40px;font-weight:600;font-size:66px;line-height:1;color:var(--sun);padding-left:20px;
  }
  .title-link{
    top:110px;font-weight:300;font-size:24px;line-height:1;color:var(--teal);padding-left:22px;
  }
  .title-second{
    top:137px;line-height:1;white-space:nowrap;padding-left:14px;
  }
  .title-second .big{font-weight:600;font-size:54px;color:var(--sun)}
  .title-second .small{font-weight:300;font-size:22px;color:var(--teal);margin-left:4px}
  .moments{
    position:absolute;left:73px;top:200px;width:266px;height:264px;
    display:grid;grid-template-columns:1fr 1fr;grid-template-rows:1fr 1fr;gap:7px;
  }
  .moment{border:3px solid var(--teal)}
  .moment-nw{border-radius:50% 50% 0 50%;border-right:0;border-bottom:0;
    background:linear-gradient(135deg,#d9c2ad,#f3e6dc 60%,#fbf7f3)}
  .moment-ne{border-radius:50% 50% 50% 0;border-color:var(--coral);border-left:0;border-bottom:0;
    background:linear-gradient(200deg,#ebe3d9,#d7a58a 55%,#c8cdd3)}
  .moment-sw{border-radius:50% 0 50% 50%;border-color:var(--coral);border-right:0;border-top:0;
    background:linear-gradient(160deg,#e2c0aa,#f1e8e2 55%,#fafafa)}
  .moment-se{border-radius:0 50% 50% 50%;border-left:0;border-top:0;
    background:linear-gradient(210deg,#f4f2ee,#e7cfc1 50%,#6b5147)}
  .tagline{
    position:absolute;left:40px;right:40px;top:473px;text-align:center;
    font-family:"Poppins",sans-serif;font-size:10.3px;line-height:1.35;color:var(--coral);
  }
</style>
</head>
<body>
  <main class="cover">
    <svg class="cover-frame" width="410" height="530" viewBox="0 0 410 530" aria-hidden="true">
      <defs>
        <linearGradient id="band-left" x1="0" y1="0" x2="0" y2="1">
          <stop offset="0" stop-color="#f29a8e"/>
          <stop offset=".5" stop-color="#fdf3e6"/>
          <stop offset="1" stop-color="#f2cc68"/>
        </linearGradient>
        <linearGradient id="band-right" x1="0" y1="0" x2="0" y2="1">
          <stop offset="0" stop-color="#f3cb66"/>
          <stop offset=".5" stop-color="#fdf3e6"/>
          <stop offset="1" stop-color="#f39a8e"/>
        </linearGradient>
      </defs>
      <path d="M0 0 H45 Q30 265 45 530 H0 Z" fill="url(#band-left)"/>
      <path d="M410 0 H365 Q380 265 365 530 H410 Z" fill="url(#band-right)"/>
      <path d="M56 0 Q38 265 56 530" fill="none" stroke="var(--line-sun)" stroke-width="1"/>
      <path d="M354 0 Q372 265 354 530" fill="none" stroke="var(--line-coral)" stroke-width="1"/>
    </svg>

    <h1>
      <span class="title title-kicker">THE CRADLE</span>
      <span class="title title-main">Compass</span>
      <span class="title title-link">to Infancy's</span>
      <span class="title title-second"><span class="big">Opening</span><span class="small">Seasons</span></span>
    </h1>

    <section class="moments">
      <div class="moment moment-nw" role="img" aria-label="Photo: a smiling parent resting cheek to cheek with a baby"></div>
      <div class="moment moment-ne" role="img" aria-label="Photo: a parent bottle-feeding a baby on a sofa"></div>
      <div class="moment moment-sw" role="img" aria-label="Photo: a parent and baby sleeping side by side"></div>
      <div class="moment moment-se" role="img" aria-label="Photo: a parent lifting a baby up playfully"></div>
    </section>

    <p class="tagline">Grounded, Research-Led Methods on Rest,<br>Nourishment, Protection plus Growing Assurance</p>
  </main>
</body>
</html>
```